Regional Showdown Flyer for Holiday Program

Need a one page flyer, can be back to front or one page, ensuring you can fit all information, colourful, aimed at a market of 8-13 year old boys and girls.
The flyer needs to be noticed, needs to have certain information on it and needs to be Autralian Rule Football orientated.
Have uploaded file so you can understand the style (not content), style of flyer I am looking at getting submitted.

Target Market(s)

8-13 year old boys and girls and their parents.

Requirements
Must have
• Regional Showdown Event
• Price for Regional Showdown Day will be $85
• Strictly Limited Places, only the best footballers should enter this challenge
• Inaugural event, be the first Regional Showdown Winner for your age!
• Do you love a challenge! Put yourself to the test!
• Are you up to it - Water Slide Goal Kicking Contest! The fastest kick in the West (tested by our very own speed gun)! Can you survive the Footy Titan Trail or Last One Standing Goal Kicking! These challenges are crazy are super fun!
• If you think you can deliver on the big stage then this is for YOU!
• All District age winners will receive prizes, awards and the adulation from all their peers!
• Year's 3-5 from 9am to 12pm
• Year's 6-8 from 1-4pm
• All challengers compete against their own age
• Lunch Provided
• Monday 16th April - Upper Tarrowby Regional Showdown Day at Tarrowby Oval
• Tuesday 17th April - North Tarrowby Regional Showdown Day at Kilmorna Reserve
• Wednesday 18th April - Yarlo Regional Showdown Day - Dunhaven Football Club
• Every Challenge Participant receives a District Football!
• Need to put all 3 District Football Logos on the bottom of the flyer, logos attached at bottom.
Nice to have
• Plenty of colour, if you can fit all information on one page that would be fine
Should not have
• Dull, boring, any footballs should be Aussie Rules footballs not NFL or soccer

```html
<!DOCTYPE html>
<html lang="en">
<head>
<meta charset="utf-8">
<title>Regional Showdown Event</title>
<link rel="stylesheet" href="https://fonts.googleapis.com/css2?family=Alfa+Slab+One&family=Oswald:wght@700&family=Raleway:wght@400;500;800&display=swap">
<style>
  :root {
    --maroon-deep: #3f0810;
    --maroon: #5a0b14;
    --crimson: #9b2029;
    --crimson-dark: #6e1219;
    --red-hot: #ff1d0e;
    --band-red: #e8161c;
    --yellow: #f7e816;
    --white: #ffffff;
    --panel: #efe6e8;
    --panel-ink: #6b1a22;
    --ball-light: #f0662a;
    --ball-dark: #a8381a;
  }
  * { margin: 0; padding: 0; box-sizing: border-box; }
  html, body { width: 927px; height: 1200px; overflow: hidden; background: var(--maroon-deep); }
  .flyer {
    position: relative; width: 927px; height: 1200px; overflow: hidden;
    background: linear-gradient(180deg, var(--crimson-dark) 0%, var(--maroon) 45%, var(--maroon-deep) 100%);
    font-family: "Raleway", sans-serif; color: var(--white);
  }
  .header-bg { position: absolute; left: 0; top: 0; width: 927px; height: 360px; }
  .title { position: absolute; left: 0; top: 30px; width: 927px; height: 280px; }
  .title .main { font-family: "Alfa Slab One", serif; fill: var(--yellow); }
  .title .sub { font-family: "Alfa Slab One", serif; fill: var(--white); }
  .tagline {
    position: absolute; top: 312px; left: 0; width: 927px; text-align: center;
    font-weight: 800; font-size: 22.5px; line-height: 30px; letter-spacing: 0.3px;
  }
  .football { position: absolute; left: 455px; top: 380px; width: 472px; height: 560px; }
  .inaugural-band {
    position: absolute; left: 0; top: 392px; width: 500px; height: 46px; background: var(--band-red);
    font-weight: 800; font-size: 34px; line-height: 46px; color: var(--yellow); padding-left: 56px; letter-spacing: 0.3px;
  }
  .first-winner {
    position: absolute; left: 0; top: 448px; width: 472px; text-align: center;
    font-weight: 800; font-size: 17px; line-height: 23px;
  }
  .challenge-panel {
    position: absolute; left: 45px; top: 512px; width: 389px; height: 362px;
    background: var(--panel); border-radius: 10px; padding: 8px 14px 0;
    color: var(--panel-ink); font-weight: 400; font-size: 13.6px; line-height: 18.5px; text-align: center; text-transform: uppercase;
  }
  .challenge-panel p { position: relative; padding: 5px 0 6px; }
  .challenge-panel p::after {
    content: ""; position: absolute; left: 38px; right: 38px; bottom: 0; border-bottom: 1.3px dashed var(--panel-ink);
  }
  .challenge-panel p:last-child::after { display: none; }
  .details-band {
    position: absolute; left: 0; top: 888px; width: 927px; height: 220px; background: var(--maroon);
  }
  .price-badge {
    position: absolute; left: 582px; top: 702px; width: 280px; height: 280px; border-radius: 50%;
    background: var(--red-hot); text-align: center;
  }
  .price-badge .label { margin-top: 38px; font-weight: 800; font-size: 18.5px; line-height: 23.5px; }
  .price-badge .amount {
    font-family: "Oswald", sans-serif; font-weight: 700; font-size: 132px; line-height: 124px; letter-spacing: -3px;
  }
  .details {
    position: absolute; left: 36px; top: 913px; list-style: none;
    font-weight: 500; font-size: 17.8px; line-height: 21.6px; text-transform: uppercase; white-space: nowrap;
  }
  .details li { position: relative; padding-left: 16px; }
  .details li::before {
    content: ""; position: absolute; left: 0; top: 9px; width: 7px; height: 7px; border-radius: 50%; background: var(--yellow);
  }
  .club-strip {
    position: absolute; left: 0; top: 1108px; width: 927px; height: 92px; background: var(--white);
    display: flex; justify-content: space-around; align-items: center; padding: 0 120px;
  }
  .club { display: flex; align-items: center; gap: 8px; font-weight: 800; font-size: 15px; text-transform: uppercase; }
  .club .dot { width: 26px; height: 26px; border-radius: 50%; }
  .club--ironbark { color: #d3141b; } .club--ironbark .dot { background: #d3141b; }
  .club--yarlo { color: #1a8a7a; } .club--yarlo .dot { background: #1a8a7a; }
  .club--stingray { color: #1d4fa0; } .club--stingray .dot { background: #1d4fa0; }
</style>
</head>
<body>
<main class="flyer">
  <svg class="header-bg" viewBox="0 0 927 360" aria-hidden="true">
    <path d="M0 0 H927 V300 Q463 270 0 340 Z" fill="#931e27"/>
  </svg>

  <svg class="title" viewBox="0 0 927 280" aria-label="Regional Showdown Event">
    <text class="main" x="464" y="154" text-anchor="middle" font-size="172" textLength="736" lengthAdjust="spacingAndGlyphs">REGIONAL</text>
    <text class="sub" x="464" y="262" text-anchor="middle" font-size="118" textLength="738" lengthAdjust="spacingAndGlyphs">SHOWDOWN EVENT</text>
  </svg>

  <p class="tagline">STRICTLY LIMITED PLACES, ONLY THE BEST<br>FOOTBALLERS SHOULD ENTER THIS CHALLENGE</p>

  <svg class="football" viewBox="0 0 472 560" role="img" aria-label="Large Australian Rules football">
    <defs>
      <radialGradient id="ballShade" cx="40%" cy="35%" r="70%">
        <stop offset="0%" stop-color="var(--ball-light)"/>
        <stop offset="100%" stop-color="var(--ball-dark)"/>
      </radialGradient>
    </defs>
    <ellipse cx="330" cy="300" rx="300" ry="215" transform="rotate(35 330 300)" fill="url(#ballShade)"/>
  </svg>

  <div class="inaugural-band">INAUGURAL EVENT</div>
  <p class="first-winner">BE THE FIRST REGIONAL SHOWDOWN<br>WINNER FOR YOUR AGE!</p>

  <section class="challenge-panel">
    <p>Do you love a challenge! Put yourself to the test!</p>
    <p>If you think you can deliver on the big stage then this is for YOU!</p>
    <p>Are you up to it - water slide goal kicking contest! The fastest kick in the west (tested by our very own speed gun)!</p>
    <p>Can you survive the Footy Titan Trail or Last One Standing goal kicking!</p>
    <p>These challenges are crazy are super fun!</p>
    <p>All District age winners will receive prizes, awards and the adulation from all their peers!</p>
  </section>

  <div class="details-band"></div>

  <div class="price-badge">
    <p class="label">PRICE FOR<br>REGIONAL<br>SHOWDOWN DAY</p>
    <p class="amount">$85</p>
  </div>

  <ul class="details">
    <li>Year's 3-5 from 9am to 12pm</li>
    <li>Year's 6-8 from 1-4pm</li>
    <li>All challengers compete against their own age</li>
    <li>Lunch provided</li>
    <li>Monday 16th April - Upper Tarrowby Regional Showdown Day at Tarrowby Oval</li>
    <li>Tuesday 17th April - North Tarrowby Regional Showdown Day at Kilmorna Reserve</li>
    <li>Wednesday 18th April - Yarlo Regional Showdown Day - Dunhaven Football Club</li>
    <li>Every challenge participant receives a District Football!</li>
  </ul>

  <footer class="club-strip">
    <div class="club club--ironbark"><span class="dot"></span>Ironbark District</div>
    <div class="club club--yarlo"><span class="dot"></span>Yarlo District</div>
    <div class="club club--stingray"><span class="dot"></span>Stingray District</div>
  </footer>
</main>
</body>
</html>
```